Velmora Energy LNG as Marine Fuel Powerpoint Design

Powerpoint template inspired by and using the attached Velmora Energy logo. We are developing LNG as marine fuel facilities and bunkering vessels to supply the fuel to the marine industry. Designs should use the Velmora Energy logo colors and be consistent with our vision of providing environmentally cleaner fuel supply. Our selected logo was 1A in the attached files, as shown on the business card template also attached.

Target Market(s)

Marine Industry (Shipping, container vessels, crude carriers, cargo / transportation vessels, etc.)

Requirements
Must have
• Clean / green energy theme
Compatibility with submitted logo and logo color scheme
Font headers that work well with the logo font
Nice to have
• Marine / Maritime theme
relevance to Gulf Coast Region
Should not have
• Dark colors

```html
<!DOCTYPE html>
<html lang="en">
<head>
<meta charset="utf-8">
<title>Velmora Energy – Presentation Deck</title>
<link href="https://fonts.googleapis.com/css2?family=Audiowide&family=Montserrat:wght@400;500;600;700;800;900&display=swap" rel="stylesheet">
<style>
:root{
  --blue:#1560a8;
  --blue-deep:#0b4a8f;
  --blue-bright:#2a8bd0;
  --navy:#1d3559;
  --green:#2f8f3e;
  --green-light:#4caf4f;
  --pink:#d1276a;
  --grey-bg:#e9e9eb;
  --grey-text:#6b6f76;
  --ink:#222;
  --white:#fff;
}
*{box-sizing:border-box;margin:0;padding:0}
html,body{width:1200px;height:2168px;overflow:hidden;background:var(--grey-bg)}
body{font-family:"Montserrat",sans-serif;color:var(--ink)}
.stage{position:relative;width:1426px;height:2576px;transform:scale(0.841515);transform-origin:0 0;background:var(--grey-bg);overflow:hidden}
.abs{position:absolute}

/* hero */
.hero-photo{position:absolute;left:0;top:0;width:1426px;height:668px;
  background:linear-gradient(180deg,#a7a19a 0%,#b9b4ae 35%,#d4d2cf 70%,var(--grey-bg) 100%);
  clip-path:polygon(0 0,100% 0,100% 30%,0 100%)}
.hero-title{position:absolute;left:84px;top:222px;text-align:center;width:470px}
.hero-title .big{display:block;font-weight:800;font-size:74px;color:var(--blue-deep);line-height:1;letter-spacing:-1px}
.hero-title .small{display:block;font-weight:400;font-size:72px;color:var(--ink);line-height:1;margin-top:2px}
.hero-rule{position:absolute;left:548px;top:635px;width:302px;height:1px;background:#5a5fa8}

/* slide base */
.slide{position:absolute;width:456px;height:257px;background:var(--white);overflow:hidden}
.c1{left:17px}.c2{left:485px}.c3{left:953px}
.r1{top:668px}.r2{top:940px}.r3{top:1213px}.r4{top:1485px}.r5{top:1757px}.r6{top:2030px}.r7{top:2302px}

.display{font-family:"Audiowide",sans-serif}
.mark{position:absolute;top:8px;right:9px;display:flex;flex-direction:column;align-items:center;gap:2px}
.mark i{display:block;width:11px;height:11px;border-radius:50%;background:var(--blue)}
.mark b{font-family:"Montserrat",sans-serif;font-weight:700;font-size:4px;color:var(--blue);letter-spacing:.2px}
.logo{display:flex;flex-direction:column;align-items:center;gap:4px}
.logo i{display:block;border-radius:50%;background:var(--blue)}
.logo b{font-weight:700;color:var(--blue);letter-spacing:.5px}

.kicker{position:absolute;left:30px;top:14px;font-size:6px;letter-spacing:3px;color:var(--grey-text)}
.slide-title{position:absolute;left:28px;top:22px;font-family:"Audiowide",sans-serif;font-size:14px;font-weight:400;color:var(--navy)}
.title-rule{position:absolute;left:30px;top:42px;width:14px;height:2px;background:var(--blue)}

.page-tab{position:absolute;right:0;bottom:0;width:78px;height:22px;background:var(--blue);border-top-left-radius:44px 22px;color:#fff;font-size:4.5px;font-weight:700;letter-spacing:1px;text-align:right;padding:11px 8px 0 0}
.wave{position:absolute;left:0;bottom:0;width:456px;height:40px}

.tiny{font-size:5px;line-height:1.45;color:var(--grey-text)}
.tiny-w{font-size:5px;line-height:1.45;color:#e3eefb}
.label-b{font-size:6.5px;font-weight:700;color:var(--blue)}
.label-g{font-size:6.5px;font-weight:700;color:var(--green)}
.photo-blue{background:linear-gradient(180deg,#3f8cc9 0%,#1a65ad 55%,#0d4f96 100%)}
.dot{position:absolute;border-radius:50%}
</style>
</head>
<body>
<div class="stage">

  <!-- hero -->
  <div class="hero-photo" role="img" aria-label="Crowd raising hands at sunset, faded background photo"></div>
  <div class="hero-title"><span class="big">Presentation</span><span class="small">Deck</span></div>

  <section class="slide" style="left:667px;top:101px;width:557px;height:313px">
    <div class="abs" style="left:0;top:0;width:557px;height:82px;background:#fff"></div>
    <div class="logo abs" style="left:0;top:12px;width:557px"><i style="width:30px;height:30px"></i><b style="font-size:8px">VELMORA ENERGY</b></div>
    <div class="abs photo-blue" style="left:0;top:82px;width:557px;height:231px" role="img" aria-label="Port with cranes and vessels in blue tint"></div>
    <p class="abs" style="left:0;top:108px;width:557px;text-align:center;color:#fff;font-size:11px;letter-spacing:4px">2020</p>
    <h2 class="abs display" style="left:0;top:176px;width:557px;text-align:center;color:#fff;font-size:19px;font-weight:400">ADD YOUR AWESOME TITLE HERE</h2>
    <p class="abs" style="left:0;top:204px;width:557px;text-align:center;color:#fff;font-size:7px;letter-spacing:4px">SUBTITLE GOES HERE</p>
  </section>
  <div class="hero-rule"></div>

  <!-- row 1 -->
  <section class="slide c1 r1">
    <div class="logo abs" style="left:0;top:6px;width:456px"><i style="width:26px;height:26px"></i><b style="font-size:6px">VELMORA ENERGY</b></div>
    <div class="abs photo-blue" style="left:0;top:67px;width:456px;height:190px" role="img" aria-label="Port with cranes and ships in blue tint"></div>
    <p class="abs" style="left:0;top:86px;width:456px;text-align:center;color:#fff;font-size:8px;letter-spacing:3px">2020</p>
    <h2 class="abs display" style="left:0;top:146px;width:456px;text-align:center;color:#fff;font-size:15px;font-weight:400">ADD YOUR AWESOME TITLE HERE</h2>
    <p class="abs" style="left:0;top:167px;width:456px;text-align:center;color:#fff;font-size:5.5px;letter-spacing:3px">SUBTITLE GOES HERE</p>
  </section>

  <section class="slide c2 r1">
    <div class="abs photo-blue" style="left:0;top:30px;width:456px;height:227px" role="img" aria-label="Harbour with cargo ship and cranes on blue water"></div>
    <svg class="abs" style="left:0;top:0" width="456" height="257" viewBox="0 0 456 257">
      <path d="M0 0H456V30C400 20 340 50 300 80C250 115 190 110 140 100C90 92 40 110 0 118Z" fill="var(--green)"/>
      <path d="M0 0H456V18C400 10 340 38 300 66C250 100 190 96 140 88C90 80 40 98 0 104Z" fill="#fff"/>
      <path d="M360 257C400 245 420 225 456 215V257Z" fill="#fff"/>
    </svg>
    <div class="logo abs" style="left:45px;top:10px"><i style="width:36px;height:36px"></i><b style="font-size:7px">VELMORA ENERGY</b></div>
    <p class="abs" style="left:243px;top:138px;color:#fff;font-size:7px;letter-spacing:4px">SUBTITLE GOES HERE</p>
    <h2 class="abs display" style="left:50px;top:149px;color:#fff;font-size:15px;font-weight:400">ADD YOUR AWESOME TITLE HERE</h2>
    <p class="abs display" style="right:16px;top:238px;color:var(--navy);font-size:8px">2020</p>
  </section>

  <section class="slide c3 r1">
    <div class="abs" style="left:0;top:0;width:45px;height:257px;background:var(--green)"></div>
    <p class="abs display" style="left:-62px;top:120px;width:170px;transform:rotate(-90deg);color:#fff;font-size:12px;text-align:center">TABLE OF CONTENT</p>
    <div class="abs" style="left:62px;top:45px;width:168px;height:168px;border-radius:50%;background:radial-gradient(circle,#7cc14f 0%,#4a9a33 70%,#e9f3e3 100%)" role="img" aria-label="Green leafy globe"></div>
    <ol class="abs" style="left:260px;top:35px;list-style:none;font-size:7.5px;color:var(--grey-text);line-height:20.5px">
      <li><span style="display:inline-block;width:27px">i.</span>Introduction</li>
      <li><span style="display:inline-block;width:27px">ii.</span>About Us</li>
      <li><span style="display:inline-block;width:27px">iii.</span>Welcome Message</li>
      <li><span style="display:inline-block;width:27px">iv.</span>Company Profile</li>
      <li><span style="display:inline-block;width:27px">v.</span>Team</li>
      <li><span style="display:inline-block;width:27px">vi.</span>Team Group</li>
      <li><span style="display:inline-block;width:27px">vii.</span>Portfolio</li>
      <li><span style="display:inline-block;width:27px">viii.</span>Info graphic</li>
      <li><span style="display:inline-block;width:27px">ix.</span>Contact Us</li>
      <li><span style="display:inline-block;width:27px">x.</span>Data Chart</li>
    </ol>
    <div class="mark"><i></i><b>VELMORA ENERGY</b></div>
    <div class="page-tab">PAGE |3</div>
  </section>

  <!-- row 2 -->
  <section class="slide c1 r2">
    <div class="abs" style="left:0;top:0;width:188px;height:257px;background:linear-gradient(135deg,#a8784a,#7a4f2c 50%,#b98a5a)" role="img" aria-label="Coiled ship rope close-up"></div>
    <div class="abs display" style="left:143px;top:34px;width:214px;height:36px;background:var(--blue);color:#fff;font-size:8px;padding:15px 0 0 20px">LOREM IPSUM CONSECTETUR</div>
    <p class="abs tiny" style="left:215px;top:97px;width:215px;text-align:justify">Business valuation is a process and a set of procedures used to estimate the economic value of an owner's interest in a business. Valuation is used by market participants to set the price they are willing to pay or receive.</p>
    <svg class="abs" style="left:217px;top:158px" width="12" height="14" viewBox="0 0 12 14"><rect x="1" y="2" width="9" height="11" fill="none" stroke="var(--green)" stroke-width="1.4"/><path d="M4 8l2 2 5-7" fill="none" stroke="var(--green)" stroke-width="1.4"/></svg>
    <svg class="abs" style="left:330px;top:160px" width="13" height="12" viewBox="0 0 13 12"><path d="M0 6L13 0 9 12 6 8Z" fill="var(--green)"/></svg>
    <p class="abs label-b" style="left:216px;top:178px">Your Contents Here</p>
    <p class="abs label-b" style="left:330px;top:176px">Your Contents Here</p>
    <p class="abs tiny" style="left:216px;top:190px;width:98px">Lorem ipsum dolor sit amet, consectetur adipiscing elit, sed do eiusmod tempor incididunt.</p>
    <p class="abs tiny" style="left:330px;top:188px;width:98px">Lorem ipsum dolor sit amet, consectetur adipiscing elit, sed do eiusmod tempor incididunt.</p>
    <div class="mark"><i></i><b>VELMORA ENERGY</b></div>
    <div class="page-tab">PAGE |4</div>
  </section>

  <section class="slide c2 r2">
    <p class="kicker">HERE ADD YOUR TITLE</p><h3 class="slide-title">ADD YOUR TITLE HERE</h3>
    <p class="abs tiny" style="left:30px;top:63px;width:390px;text-align:justify;line-height:1.95">Lorem ipsum dolor sit amet, consectetur adipiscing elit. Fusce sit amet neque sodales, faucibus ex eu, efficitur lacus. Cras imperdiet, nulla nec sagittis pulvinar, neque augue iaculis risus, ac fringilla felis urna fermentum mi. Ut vehicula vel enim sit amet vulputate. Aenean malesuada consectetur diam, ac convallis quam tincidunt eget. Nam vitae elementum ipsum. Proin vitae blandit enim. Donec congue convallis commodo. Aenean vel lacus lacus. Sed in erat ultrices dolor faucibus feugiat. Nullam cursus sollicitudin dictum. Donec a ex at enim consectetur auctor. Aliquam ut laoreet neque. Aenean molestie, libero sed suscipit tincidunt, tellus nulla dictum dui, in viverra nunc purus sodales diam. Sed ullamcorper at ante eget euismod. Sed in erat ultrices dolor faucibus feugiat. Nullam cursus sollicitudin dictum. Donec a ex at enim consectetur auctor tellus nulla.</p>
    <p class="abs tiny" style="left:30px;top:184px;width:390px;text-align:justify;line-height:1.95">Maecenas in purus at tellus tincidunt sodales eu sed nibh. Aenean justo diam, commodo vel felis ac, malesuada sodales purus. Nunc sollicitudin sed justo in eleifend. Fusce dictum ornare ligula, eu porttitor elit ullamcorper non.</p>
    <svg class="wave" viewBox="0 0 456 40" preserveAspectRatio="none"><path d="M0 26C140 4 300 6 456 18V26C300 14 140 14 0 34Z" fill="var(--green)"/><path d="M0 34C140 14 300 16 456 26V40H0Z" fill="var(--blue)"/></svg>
    <div class="mark"><i></i><b>VELMORA ENERGY</b></div>
    <div class="page-tab">PAGE |5</div>
  </section>

  <section class="slide c3 r2">
    <div class="abs" style="left:42px;top:44px;width:30px;height:2px;background:var(--green)"></div>
    <p class="abs display" style="left:42px;top:48px;width:230px;color:var(--blue);font-size:9px;line-height:1.3">SUCCESS IS NOT ONLY WHAT YOU ACHIEVE IN YOUR LIFE, BUT ALSO WHAT YOU INSPIRE IN THE LIVES OF OTHERS</p>
    <div class="abs photo-blue" style="left:0;top:128px;width:456px;height:129px" role="img" aria-label="Blue tinted crowd photo"></div>
    <p class="abs" style="left:42px;top:164px;color:#fff;font-size:7px;font-weight:600">Lorem ipsum dolor</p>
    <p class="abs" style="left:176px;top:164px;color:#fff;font-size:7px;font-weight:600">Lorem ipsum dolor</p>
    <p class="abs" style="left:307px;top:164px;color:#fff;font-size:7px;font-weight:600">Lorem ipsum dolor</p>
    <p class="abs tiny-w" style="left:42px;top:185px;width:110px">Lorem ipsum dolor sit amet, consectetur adipiscing elit, sed do eiusmod tempor</p>
    <p class="abs tiny-w" style="left:176px;top:185px;width:110px">Lorem ipsum dolor sit amet, consectetur adipiscing elit, sed do eiusmod tempor</p>
    <p class="abs tiny-w" style="left:307px;top:185px;width:110px">Lorem ipsum dolor sit amet, consectetur adipiscing elit, sed do eiusmod tempor</p>
  </section>

  <!-- row 3 -->
  <section class="slide c1 r3">
    <p class="kicker">HERE ADD YOUR TITLE</p><h3 class="slide-title">ADD YOUR TITLE HERE</h3><span class="title-rule"></span>
    <svg class="abs" style="left:168px;top:58px" width="116" height="180" viewBox="0 0 116 180">
      <path d="M58 0L84 44H32Z" fill="var(--blue-bright)"/>
      <path d="M30 48H86L100 86H16Z" fill="var(--blue-deep)"/>
      <path d="M14 90H102Q104 112 100 130H16Q12 112 14 90Z" fill="var(--green-light)"/>
      <path d="M16 134H100Q96 170 58 172Q20 170 16 134Z" fill="var(--green)"/>
      <text x="58" y="36" font-size="5" fill="#fff" text-anchor="middle" font-family="Montserrat">Content</text>
      <text x="58" y="42" font-size="5" fill="#fff" text-anchor="middle" font-family="Montserrat">Title</text>
      <text x="58" y="70" font-size="5" fill="#fff" text-anchor="middle" font-family="Montserrat">Content Title</text>
      <text x="58" y="113" font-size="5" fill="#fff" text-anchor="middle" font-family="Montserrat">Content Title</text>
      <text x="58" y="155" font-size="5" fill="#fff" text-anchor="middle" font-family="Montserrat">Content Title</text>
    </svg>
    <svg class="abs" style="left:0;top:0" width="456" height="257"><g stroke="#888" stroke-width=".6" stroke-dasharray="1.5 1.5"><path d="M250 84H310"/><path d="M135 113H180"/><path d="M270 155H310"/><path d="M135 197H160"/></g></svg>
    <p class="abs label-g" style="left:315px;top:72px">Content Title</p><p class="abs tiny" style="left:315px;top:82px;width:102px">Lorem ipsum randomised words which don't look even slightly believable in some form, by injected humour.</p>
    <p class="abs label-g" style="left:30px;top:108px">Content Title</p><p class="abs tiny" style="left:30px;top:118px;width:102px">Lorem ipsum randomised words which don't look even slightly believable in some form, by injected humour.</p>
    <p class="abs label-g" style="left:315px;top:155px">Content Title</p><p class="abs tiny" style="left:315px;top:165px;width:102px">Lorem ipsum randomised words which don't look even slightly believable in some form, by injected humour.</p>
    <p class="abs label-g" style="left:30px;top:192px">Content Title</p><p class="abs tiny" style="left:30px;top:202px;width:102px">Lorem ipsum randomised words which don't look even slightly believable in some form, by injected humour.</p>
    <div class="mark"><i></i><b>VELMORA ENERGY</b></div>
    <div class="page-tab">PAGE |7</div>
  </section>

  <section class="slide c2 r3">
    <div class="abs" style="left:0;top:0;width:456px;height:130px;background:linear-gradient(90deg,var(--blue-deep),var(--blue))"></div>
    <h3 class="abs display" style="left:0;top:30px;width:456px;text-align:center;color:#fff;font-size:22px;font-weight:400">OUR SERVICES</h3>
    <p class="abs" style="left:0;top:62px;width:456px;text-align:center;color:#fff;font-size:7px;letter-spacing:3px">SUB TITLE GOES HERE</p>
    <div class="dot" style="left:79px;top:101px;width:48px;height:48px;background:#fff;box-shadow:0 2px 6px rgba(0,0,0,.2)"></div>
    <div class="dot" style="left:204px;top:101px;width:48px;height:48px;background:#fff;box-shadow:0 2px 6px rgba(0,0,0,.2)"></div>
    <div class="dot" style="left:330px;top:101px;width:48px;height:48px;background:#fff;box-shadow:0 2px 6px rgba(0,0,0,.2)"></div>
    <svg class="abs" style="left:93px;top:115px" width="20" height="20" viewBox="0 0 20 20"><path d="M2 13H18L15 18H5Z" fill="var(--blue)"/><rect x="7" y="6" width="6" height="6" fill="var(--blue)"/></svg>
    <svg class="abs" style="left:218px;top:115px" width="20" height="20" viewBox="0 0 20 20"><path d="M10 2C14 7 16 10 16 13A6 6 0 0 1 4 13C4 10 6 7 10 2Z" fill="var(--blue)"/></svg>
    <svg class="abs" style="left:344px;top:115px" width="20" height="20" viewBox="0 0 20 20"><rect x="4" y="3" width="12" height="14" fill="var(--blue)"/><circle cx="10" cy="11" r="3" fill="#fff"/></svg>
    <p class="abs label-g" style="left:60px;top:157px;width:86px;text-align:center">Contents Title</p>
    <p class="abs label-g" style="left:185px;top:157px;width:86px;text-align:center">Contents Title</p>
    <p class="abs label-g" style="left:311px;top:157px;width:86px;text-align:center">Contents Title</p>
    <p class="abs tiny" style="left:58px;top:169px;width:90px;text-align:center">Lorem ipsum randomised words which don't look even slightly believable in some form, by injected humour.</p>
    <p class="abs tiny" style="left:183px;top:169px;width:90px;text-align:center">Lorem ipsum randomised words which don't look even slightly believable in some form, by injected humour.</p>
    <p class="abs tiny" style="left:309px;top:169px;width:90px;text-align:center">Lorem ipsum randomised words which don't look even slightly believable in some form, by injected humour.</p>
    <div class="page-tab">PAGE |8</div>
  </section>

  <section class="slide c3 r3">
    <p class="kicker">HERE ADD YOUR TITLE</p><h3 class="slide-title">ADD YOUR TITLE HERE</h3><span class="title-rule"></span>
    <div class="dot" style="left:27px;top:79px;width:20px;height:20px;background:var(--blue-deep);color:#fff;font-size:7px;text-align:center;line-height:20px">1</div>
    <div class="dot" style="left:27px;top:123px;width:20px;height:20px;background:var(--blue-deep);color:#fff;font-size:7px;text-align:center;line-height:20px">2</div>
    <div class="dot" style="left:27px;top:167px;width:20px;height:20px;background:var(--blue-deep);color:#fff;font-size:7px;text-align:center;line-height:20px">3</div>
    <div class="dot" style="left:226px;top:79px;width:20px;height:20px;background:var(--green);color:#fff;font-size:7px;text-align:center;line-height:20px">5</div>
    <div class="dot" style="left:226px;top:123px;width:20px;height:20px;background:var(--green);color:#fff;font-size:7px;text-align:center;line-height:20px">6</div>
    <div class="dot" style="left:226px;top:167px;width:20px;height:20px;background:var(--green);color:#fff;font-size:7px;text-align:center;line-height:20px">7</div>
    <p class="abs label-g" style="left:57px;top:71px">Contents Title</p><p class="abs tiny" style="left:57px;top:80px;width:140px">Lorem ipsum randomised words which don't look even slightly believable in some form, by injected humour.</p>
    <p class="abs label-g" style="left:57px;top:115px">Contents Title</p><p class="abs tiny" style="left:57px;top:124px;width:140px">Lorem ipsum randomised words which don't look even slightly believable in some form, by injected humour.</p>
    <p class="abs label-g" style="left:57px;top:160px">Contents Title</p><p class="abs tiny" style="left:57px;top:169px;width:140px">Lorem ipsum randomised words which don't look even slightly believable in some form, by injected humour.</p>
    <p class="abs label-g" style="left:256px;top:71px">Contents Title</p><p class="abs tiny" style="left:256px;top:80px;width:140px">Lorem ipsum randomised words which don't look even slightly believable in some form, by injected humour.</p>
    <p class="abs label-g" style="left:256px;top:115px">Contents Title</p><p class="abs tiny" style="left:256px;top:124px;width:140px">Lorem ipsum randomised words which don't look even slightly believable in some form, by injected humour.</p>
    <p class="abs label-g" style="left:256px;top:160px">Contents Title</p><p class="abs tiny" style="left:256px;top:169px;width:140px">Lorem ipsum randomised words which don't look even slightly believable in some form, by injected humour.</p>
    <svg class="wave" viewBox="0 0 456 40" preserveAspectRatio="none"><path d="M0 26C140 4 300 6 456 18V26C300 14 140 14 0 34Z" fill="var(--green)"/><path d="M0 34C140 14 300 16 456 26V40H0Z" fill="var(--blue)"/></svg>
    <div class="mark"><i></i><b>VELMORA ENERGY</b></div>
    <div class="page-tab">PAGE |9</div>
  </section>

  <!-- row 4 -->
  <section class="slide c1 r4" style="background:linear-gradient(90deg,var(--blue-deep),var(--blue))">
    <h3 class="abs display" style="left:33px;top:108px;color:#fff;font-size:24px;font-weight:400">PAGE BREAK</h3>
    <div class="abs" style="left:33px;top:146px;width:20px;height:3px;background:var(--green-light)"></div>
    <p class="abs tiny-w" style="left:33px;top:153px;width:250px">Lorem ipsum dolor sit amet, consectetur adipiscing elit, sed do eiusmod tempor incididunt ut labore et dolore magna aliqua. Ut enim ad minim veniam, quis nostrud exercitation ullamco laboris nisi aliquip.</p>
  </section>

  <section class="slide c2 r4">
    <h3 class="abs display" style="left:23px;top:34px;color:var(--navy);font-size:12px;font-weight:400;line-height:1.05">LOREM IPSUM<br>DOLOR SIT AMET<br>ELIT ET DOLOR</h3>
    <p class="abs tiny" style="left:23px;top:85px;width:140px">Lorem ipsum dolor sit amet, consectetur adipiscing elit, sed do eiusmod tempor incididunt ut labore et dolore magna aliqua, consectetur adipiscing elit, sed do eiusmod.</p>
    <div class="abs" style="left:217px;top:10px;width:220px;height:150px;background:linear-gradient(180deg,#cfe0ee 0%,#9fc0da 50%,#4f8fbf 100%)" role="img" aria-label="Container ship sailing on open sea"></div>
    <div class="abs" style="left:0;top:150px;width:153px;height:107px;background:var(--blue-deep)"></div>
    <div class="abs" style="left:153px;top:150px;width:150px;height:107px;background:var(--green)"></div>
    <div class="abs" style="left:303px;top:150px;width:153px;height:107px;background:var(--blue-deep)"></div>
    <div class="dot" style="left:22px;top:134px;width:30px;height:30px;background:var(--blue-bright);border:2px solid #fff"></div>
    <div class="dot" style="left:175px;top:134px;width:30px;height:30px;background:var(--green-light);border:2px solid #fff"></div>
    <div class="dot" style="left:325px;top:134px;width:30px;height:30px;background:var(--blue-bright);border:2px solid #fff"></div>
    <p class="abs" style="left:20px;top:180px;color:#fff;font-size:6.5px;font-weight:700">Lorem ipsum dolor</p>
    <p class="abs" style="left:170px;top:180px;color:#fff;font-size:6.5px;font-weight:700">Lorem ipsum dolor</p>
    <p class="abs" style="left:320px;top:180px;color:#fff;font-size:6.5px;font-weight:700">Lorem ipsum dolor</p>
    <p class="abs tiny-w" style="left:20px;top:191px;width:122px">Lorem ipsum dolor sit amet, consectetur adipiscing elit, sed do eiusmod tempor incididunt ut labore et dolore magna aliqua.</p>
    <p class="abs tiny-w" style="left:170px;top:191px;width:122px">Lorem ipsum dolor sit amet, consectetur adipiscing elit, sed do eiusmod tempor incididunt ut labore et dolore magna aliqua.</p>
    <p class="abs tiny-w" style="left:320px;top:191px;width:122px">Lorem ipsum dolor sit amet, consectetur adipiscing elit, sed do eiusmod tempor incididunt ut labore et dolore magna aliqua.</p>
    <div class="mark"><i></i><b>VELMORA ENERGY</b></div>
  </section>

  <section class="slide c3 r4">
    <div class="abs" style="left:0;top:0;width:22px;height:22px;background:var(--blue);border-bottom-right-radius:22px"></div>
    <div class="abs" style="left:30px;top:25px;width:198px;height:82px;background:linear-gradient(135deg,var(--blue-deep),#2366b5);border-radius:3px"></div>
    <p class="abs" style="left:43px;top:40px;color:#fff;font-size:6.5px;font-weight:700">Lorem ipsum dolor</p>
    <p class="abs tiny-w" style="left:43px;top:51px;width:170px">Lorem ipsum dolor sit amet, consectetur adipiscing elit, sed do eiusmod tempor incididunt ut labore et dolore magna aliqua. Lorem ipsum dolor sit amet, consectetur adipiscing elit, sed do eiusmod tempor.</p>
    <p class="abs tiny" style="left:250px;top:42px;width:160px">Lorem ipsum dolor sit amet, consectetur adipiscing elit, sed do eiusmod tempor incididunt ut labore et dolore magna aliqua. Lorem ipsum dolor sit amet, consectetur adipiscing elit, sed do eiusmod tempor incididunt ut labore et dolore magna aliqua.</p>
    <p class="abs" style="left:48px;top:134px;font-size:6px;letter-spacing:3px;color:var(--grey-text)">SUB TITLE GOES HERE</p>
    <h3 class="abs display" style="left:44px;top:144px;width:140px;text-align:center;color:var(--navy);font-size:14px;font-weight:400;line-height:1.15">YOUR TITLE<br>GOES HERE</h3>
    <div class="abs" style="left:230px;top:126px;width:193px;height:82px;background:linear-gradient(135deg,var(--green),var(--green-light));border-radius:3px"></div>
    <p class="abs" style="left:243px;top:140px;color:#fff;font-size:6.5px;font-weight:700">Lorem ipsum dolor</p>
    <p class="abs tiny-w" style="left:243px;top:151px;width:168px">Lorem ipsum dolor sit amet, consectetur adipiscing elit, sed do eiusmod tempor incididunt ut labore et dolore magna aliqua. Lorem ipsum dolor sit amet, consectetur adipiscing elit, sed do eiusmod tempor.</p>
    <div class="mark"><i></i><b>VELMORA ENERGY</b></div>
    <div class="page-tab">PAGE |13</div>
  </section>

  <!-- row 5 -->
  <section class="slide c1 r5">
    <p class="kicker" style="left:22px">HERE ADD YOUR TITLE</p><h3 class="slide-title" style="left:20px">ADD YOUR TITLE HERE</h3><span class="title-rule" style="left:22px"></span>
    <div class="dot" style="left:167px;top:66px;width:118px;height:118px;border:1px dashed #9bb"></div>
    <div class="dot" style="left:184px;top:83px;width:84px;height:84px;background:linear-gradient(135deg,var(--green-light),var(--green))"></div>
    <p class="abs" style="left:184px;top:111px;width:84px;text-align:center;color:#fff;font-size:7px;font-weight:700;line-height:1.3">Add Your<br>Awesome Title<br>Here</p>
    <div class="dot" style="left:168px;top:90px;width:9px;height:9px;background:#fff;border:2px solid var(--blue)"></div>
    <div class="dot" style="left:157px;top:120px;width:9px;height:9px;background:#fff;border:2px solid var(--blue)"></div>
    <div class="dot" style="left:168px;top:150px;width:9px;height:9px;background:#fff;border:2px solid var(--blue)"></div>
    <div class="dot" style="left:275px;top:90px;width:9px;height:9px;background:#fff;border:2px solid var(--blue)"></div>
    <div class="dot" style="left:286px;top:120px;width:9px;height:9px;background:#fff;border:2px solid var(--blue)"></div>
    <div class="dot" style="left:275px;top:150px;width:9px;height:9px;background:#fff;border:2px solid var(--blue)"></div>
    <div class="abs" style="left:62px;top:80px;width:62px;height:26px;border-radius:13px;background:var(--blue);color:#fff;font-size:4px;text-align:center;line-height:26px">Composition of the Board</div>
    <div class="abs" style="left:53px;top:111px;width:62px;height:26px;border-radius:13px;background:var(--blue);color:#fff;font-size:4px;text-align:center;padding-top:9px;line-height:1.3">Clarity of roles &amp; responsibilities</div>
    <div class="abs" style="left:62px;top:142px;width:62px;height:26px;border-radius:13px;background:var(--blue);color:#fff;font-size:4px;text-align:center;line-height:26px">Joint vision</div>
    <div class="abs" style="left:293px;top:80px;width:62px;height:26px;border-radius:13px;background:var(--blue);color:#fff;font-size:4px;text-align:center;padding-top:8px;line-height:1.3">Ability to use the strengths of all members</div>
    <div class="abs" style="left:302px;top:111px;width:66px;height:26px;border-radius:13px;background:var(--blue);color:#fff;font-size:4px;text-align:center;padding-top:8px;line-height:1.3">Ability to resolve conflicts between the board and staff</div>
    <div class="abs" style="left:293px;top:142px;width:62px;height:26px;border-radius:13px;background:var(--blue);color:#fff;font-size:4px;text-align:center;padding-top:9px;line-height:1.3">Structure &amp; organisation of the work</div>
    <svg class="wave" viewBox="0 0 456 40" preserveAspectRatio="none"><path d="M0 26C140 4 300 6 456 18V26C300 14 140 14 0 34Z" fill="var(--green)"/><path d="M0 34C140 14 300 16 456 26V40H0Z" fill="var(--blue)"/></svg>
    <div class="mark"><i></i><b>VELMORA ENERGY</b></div>
  </section>

  <section class="slide c2 r5">
    <div class="abs" style="left:0;top:0;width:22px;height:22px;background:var(--blue);border-bottom-right-radius:22px"></div>
    <p class="kicker" style="left:22px">HERE ADD YOUR TITLE</p><h3 class="slide-title" style="left:20px">ADD YOUR TITLE HERE</h3><span class="title-rule" style="left:22px"></span>
    <div class="abs" style="left:42px;top:117px;width:370px;height:1px;background:#ccc"></div>
    <div class="dot" style="left:38px;top:112px;width:11px;height:11px;background:var(--blue)"></div>
    <div class="dot" style="left:112px;top:112px;width:11px;height:11px;background:var(--green)"></div>
    <div class="dot" style="left:186px;top:112px;width:11px;height:11px;background:var(--blue)"></div>
    <div class="dot" style="left:260px;top:112px;width:11px;height:11px;background:var(--green)"></div>
    <div class="dot" style="left:334px;top:112px;width:11px;height:11px;background:var(--blue)"></div>
    <div class="dot" style="left:405px;top:112px;width:11px;height:11px;background:var(--green)"></div>
    <p class="abs" style="left:24px;top:100px;width:40px;text-align:center;font-size:6px;font-weight:700;color:var(--navy)">2015</p>
    <p class="abs" style="left:98px;top:97px;width:40px;text-align:center;font-size:6px;font-weight:700;color:var(--navy)">2016</p>
    <p class="abs" style="left:172px;top:100px;width:40px;text-align:center;font-size:6px;font-weight:700;color:var(--navy)">2017</p>
    <p class="abs" style="left:246px;top:97px;width:40px;text-align:center;font-size:6px;font-weight:700;color:var(--navy)">2018</p>
    <p class="abs" style="left:320px;top:97px;width:40px;text-align:center;font-size:6px;font-weight:700;color:var(--navy)">2019</p>
    <p class="abs" style="left:391px;top:100px;width:40px;text-align:center;font-size:6px;font-weight:700;color:var(--navy)">2020</p>
    <div class="abs" style="left:43px;top:127px;width:1px;height:12px;background:#ccc"></div>
    <div class="abs" style="left:117px;top:127px;width:1px;height:12px;background:#ccc"></div>
    <div class="abs" style="left:191px;top:127px;width:1px;height:12px;background:#ccc"></div>
    <div class="abs" style="left:265px;top:127px;width:1px;height:12px;background:#ccc"></div>
    <div class="abs" style="left:339px;top:127px;width:1px;height:12px;background:#ccc"></div>
    <div class="abs" style="left:410px;top:127px;width:1px;height:12px;background:#ccc"></div>
    <p class="abs tiny" style="left:12px;top:146px;width:64px;text-align:center"><b style="color:#333">Project name</b><br>Lorem Ipsum is simply dummy unknown printer took a galley of type and scrambled it to make</p>
    <p class="abs tiny" style="left:86px;top:146px;width:64px;text-align:center"><b style="color:#333">Project name</b><br>Lorem Ipsum is simply dummy unknown printer took a galley of type and scrambled it to make</p>
    <p class="abs tiny" style="left:160px;top:146px;width:64px;text-align:center"><b style="color:#333">Project name</b><br>Lorem Ipsum is simply dummy unknown printer took a galley of type and scrambled it to make</p>
    <p class="abs tiny" style="left:234px;top:146px;width:64px;text-align:center"><b style="color:#333">Project name</b><br>Lorem Ipsum is simply dummy unknown printer took a galley of type and scrambled it to make</p>
    <p class="abs tiny" style="left:308px;top:146px;width:64px;text-align:center"><b style="color:#333">Project name</b><br>Lorem Ipsum is simply dummy unknown printer took a galley of type and scrambled it to make</p>
    <p class="abs tiny" style="left:380px;top:146px;width:64px;text-align:center"><b style="color:#333">Project name</b><br>Lorem Ipsum is simply dummy unknown printer took a galley of type and scrambled it to make</p>
    <div class="mark"><i></i><b>VELMORA ENERGY</b></div>
    <div class="page-tab">PAGE |14</div>
  </section>

  <section class="slide c3 r5">
    <div class="abs" style="left:0;top:0;width:22px;height:22px;background:var(--blue);border-bottom-right-radius:22px"></div>
    <p class="kicker" style="left:22px">HERE ADD YOUR TITLE</p><h3 class="slide-title" style="left:20px">ADD YOUR TITLE HERE</h3><span class="title-rule" style="left:22px"></span>
    <div class="abs" style="left:14px;top:58px;width:94px;height:160px;background:#f4f5f6;border-bottom:3px solid var(--green)"></div>
    <div class="abs" style="left:119px;top:58px;width:94px;height:160px;background:#f4f5f6;border-bottom:3px solid var(--green)"></div>
    <div class="abs" style="left:224px;top:58px;width:94px;height:160px;background:#f4f5f6;border-bottom:3px solid var(--green)"></div>
    <div class="abs" style="left:329px;top:58px;width:94px;height:160px;background:#f4f5f6;border-bottom:3px solid var(--green)"></div>
    <div class="dot" style="left:17px;top:62px;width:46px;height:46px;background:#6f7a84" role="img" aria-label="Team member portrait"></div>
    <div class="dot" style="left:122px;top:62px;width:46px;height:46px;background:#6f7a84" role="img" aria-label="Team member portrait"></div>
    <div class="dot" style="left:227px;top:62px;width:46px;height:46px;background:#6f7a84" role="img" aria-label="Team member portrait"></div>
    <div class="dot" style="left:332px;top:62px;width:46px;height:46px;background:#6f7a84" role="img" aria-label="Team member portrait"></div>
    <p class="abs display" style="left:20px;top:112px;font-size:5.5px;color:var(--green)">YOUR NAME</p><p class="abs" style="left:20px;top:120px;font-size:5.5px;color:var(--grey-text)">Founder</p>
    <p class="abs display" style="left:125px;top:112px;font-size:5.5px;color:var(--green)">YOUR NAME</p><p class="abs" style="left:125px;top:120px;font-size:5.5px;color:var(--grey-text)">Global Account Executive</p>
    <p class="abs display" style="left:230px;top:112px;font-size:5.5px;color:var(--green)">YOUR NAME</p><p class="abs" style="left:230px;top:120px;font-size:5.5px;color:var(--grey-text)">Founder</p>
    <p class="abs display" style="left:335px;top:112px;font-size:5.5px;color:var(--green)">YOUR NAME</p><p class="abs" style="left:335px;top:120px;font-size:5.5px;color:var(--grey-text)">Global Account Executive</p>
    <p class="abs tiny" style="left:20px;top:140px;width:80px">Lorem ipsum dolor sit amet, consectetur adipiscing elit. Donec mauris lorem, vestibulum ac rutrum id, suscipit in dui.</p>
    <p class="abs tiny" style="left:125px;top:140px;width:80px">Lorem ipsum dolor sit amet, consectetur adipiscing elit. Donec mauris lorem, vestibulum ac rutrum id, suscipit in dui.</p>
    <p class="abs tiny" style="left:230px;top:140px;width:80px">Lorem ipsum dolor sit amet, consectetur adipiscing elit. Donec mauris lorem, vestibulum ac rutrum id, suscipit in dui.</p>
    <p class="abs tiny" style="left:335px;top:140px;width:80px">Lorem ipsum dolor sit amet, consectetur adipiscing elit. Donec mauris lorem, vestibulum ac rutrum id, suscipit in dui.</p>
    <div class="mark"><i></i><b>VELMORA ENERGY</b></div>
    <div class="page-tab">PAGE |15</div>
  </section>

  <!-- row 6 -->
  <section class="slide c1 r6">
    <p class="kicker" style="left:24px">HERE ADD YOUR TITLE</p><h3 class="slide-title" style="left:22px">ADD YOUR TITLE HERE</h3><span class="title-rule" style="left:24px"></span>
    <div class="abs display" style="left:30px;top:62px;width:60px;height:24px;background:var(--blue);border-radius:3px;color:#fff;font-size:4.5px;text-align:center;padding-top:7px;line-height:1.1">BUSINESS<br>VALUATION</div>
    <div class="abs display" style="left:30px;top:91px;width:60px;height:24px;background:var(--green);border-radius:3px;color:#fff;font-size:4.5px;text-align:center;padding-top:7px;line-height:1.1">BUSINESS<br>VALUATION</div>
    <div class="abs display" style="left:30px;top:120px;width:60px;height:24px;background:var(--blue);border-radius:3px;color:#fff;font-size:4.5px;text-align:center;padding-top:7px;line-height:1.1">BUSINESS<br>VALUATION</div>
    <div class="abs display" style="left:30px;top:149px;width:60px;height:24px;background:var(--green);border-radius:3px;color:#fff;font-size:4.5px;text-align:center;padding-top:7px;line-height:1.1">BUSINESS<br>VALUATION</div>
    <p class="abs tiny" style="left:98px;top:62px;width:330px">Lorem ipsum dolor sit amet, consectetur adipiscing elit, sed do eiusmod tempor incididunt ut labore et dolore magna aliqua. Lorem ipsum dolor sit amet, consectetur adipiscing elit, sed do eiusmod tempor incididunt ut labore et dolore magna aliqua.</p>
    <p class="abs tiny" style="left:98px;top:91px;width:330px">Lorem ipsum dolor sit amet, consectetur adipiscing elit, sed do eiusmod tempor incididunt ut labore et dolore magna aliqua. Lorem ipsum dolor sit amet, consectetur adipiscing elit, sed do eiusmod tempor incididunt ut labore et dolore magna aliqua.</p>
    <p class="abs tiny" style="left:98px;top:120px;width:330px">Lorem ipsum dolor sit amet, consectetur adipiscing elit, sed do eiusmod tempor incididunt ut labore et dolore magna aliqua. Lorem ipsum dolor sit amet, consectetur adipiscing elit, sed do eiusmod tempor incididunt ut labore et dolore magna aliqua.</p>
    <p class="abs tiny" style="left:98px;top:149px;width:330px">Lorem ipsum dolor sit amet, consectetur adipiscing elit, sed do eiusmod tempor incididunt ut labore et dolore magna aliqua. Lorem ipsum dolor sit amet, consectetur adipiscing elit, sed do eiusmod tempor incididunt ut labore et dolore magna aliqua.</p>
    <svg class="wave" viewBox="0 0 456 40" preserveAspectRatio="none"><path d="M0 26C140 4 300 6 456 18V26C300 14 140 14 0 34Z" fill="var(--green)"/><path d="M0 34C140 14 300 16 456 26V40H0Z" fill="var(--blue)"/></svg>
    <div class="mark"><i></i><b>VELMORA ENERGY</b></div>
    <div class="page-tab">PAGE |16</div>
  </section>

  <section class="slide c2 r6">
    <p class="kicker" style="left:22px">HERE ADD YOUR TITLE</p><h3 class="slide-title" style="left:20px">ADD YOUR TITLE HERE</h3><span class="title-rule" style="left:22px"></span>
    <svg class="abs" style="left:0;top:0" width="456" height="257" viewBox="0 0 456 257" font-family="Montserrat">
      <g stroke="#e2e2e2" stroke-width=".5"><path d="M40 62H430M40 77H430M40 91H430M40 106H430M40 120H430M40 135H430"/></g>
      <path d="M40 149H430" stroke="#999" stroke-width=".6"/>
      <g font-size="4.5" fill="#777" text-anchor="end"><text x="36" y="151">0</text><text x="36" y="137">1</text><text x="36" y="122">2</text><text x="36" y="108">3</text><text x="36" y="93">4</text><text x="36" y="79">5</text><text x="36" y="64">6</text></g>
      <g fill="var(--blue)"><rect x="55" y="86" width="14" height="63"/><rect x="143" y="113" width="14" height="36"/><rect x="231" y="98" width="14" height="51"/><rect x="319" y="83" width="14" height="66"/></g>
      <g fill="var(--green)"><rect x="71" y="114" width="14" height="35"/><rect x="159" y="85" width="14" height="64"/><rect x="247" y="123" width="14" height="26"/><rect x="335" y="108" width="14" height="41"/></g>
      <g fill="var(--pink)"><rect x="87" y="120" width="14" height="29"/><rect x="175" y="120" width="14" height="29"/><rect x="263" y="108" width="14" height="41"/><rect x="351" y="76" width="14" height="73"/></g>
      <g font-size="4" fill="#777" text-anchor="middle"><text x="78" y="158">Category 1</text><text x="166" y="158">Category 2</text><text x="254" y="158">Category 3</text><text x="342" y="158">Category 4</text></g>
      <g font-size="4" fill="#777"><rect x="156" y="166" width="3" height="3" fill="var(--blue)"/><text x="161" y="169">Series 1</text><rect x="186" y="166" width="3" height="3" fill="var(--green)"/><text x="191" y="169">Series 2</text><rect x="216" y="166" width="3" height="3" fill="var(--pink)"/><text x="221" y="169">Series 3</text></g>
    </svg>
    <svg class="wave" viewBox="0 0 456 40" preserveAspectRatio="none"><path d="M0 26C140 4 300 6 456 18V26C300 14 140 14 0 34Z" fill="var(--green)"/><path d="M0 34C140 14 300 16 456 26V40H0Z" fill="var(--blue)"/></svg>
    <div class="mark"><i></i><b>VELMORA ENERGY</b></div>
    <div class="page-tab">PAGE |17</div>
  </section>

  <section class="slide c3 r6">
    <p class="kicker" style="left:22px">HERE ADD YOUR TITLE</p><h3 class="slide-title" style="left:20px">ADD YOUR TITLE HERE</h3><span class="title-rule" style="left:22px"></span>
    <div class="abs" style="left:34px;top:70px;width:392px;height:150px;background:#f2f3f4"></div>
    <div class="abs display" style="left:34px;top:70px;width:80px;height:18px;background:var(--green);color:#fff;font-size:5px;text-align:center;line-height:18px">ADD YOUR TITLE</div>
    <div class="abs display" style="left:114px;top:70px;width:80px;height:18px;background:var(--green);color:#fff;font-size:5px;text-align:center;line-height:18px">ADD YOUR TITLE</div>
    <div class="abs" style="left:194px;top:64px;width:80px;height:160px;background:var(--blue-deep)"></div>
    <div class="abs" style="left:194px;top:64px;width:80px;height:24px;background:#fff;color:var(--blue);font-size:6px;font-weight:700;text-align:center;line-height:24px">VELMORA ENERGY</div>
    <div class="abs display" style="left:274px;top:70px;width:80px;height:18px;background:var(--green);color:#fff;font-size:5px;text-align:center;line-height:18px">ADD YOUR TITLE</div>
    <p class="abs tiny" style="left:40px;top:94px;width:68px"><b style="color:#333">Project name</b><br>Lorem Ipsum is simply dummy unknown printer took a galley of type and scrambled it to make.</p>
    <p class="abs tiny" style="left:40px;top:140px;width:68px"><b style="color:#333">Project name</b><br>Lorem Ipsum is simply dummy unknown printer took a galley of type and scrambled it to make.</p>
    <p class="abs tiny" style="left:120px;top:94px;width:68px"><b style="color:#333">Project name</b><br>Lorem Ipsum is simply dummy unknown printer took a galley of type and scrambled it to make.</p>
    <p class="abs tiny" style="left:120px;top:140px;width:68px"><b style="color:#333">Project name</b><br>Lorem Ipsum is simply dummy unknown printer took a galley of type and scrambled it to make.</p>
    <p class="abs tiny-w" style="left:200px;top:94px;width:68px"><b>Project name</b><br>Lorem Ipsum is simply dummy unknown printer took a galley of type and scrambled it to make.</p>
    <p class="abs tiny-w" style="left:200px;top:140px;width:68px"><b>Project name</b><br>Lorem Ipsum is simply dummy unknown printer took a galley of type and scrambled it to make.</p>
    <p class="abs tiny" style="left:280px;top:94px;width:68px"><b style="color:#333">Project name</b><br>Lorem Ipsum is simply dummy unknown printer took a galley of type and scrambled it to make.</p>
    <p class="abs tiny" style="left:280px;top:140px;width:68px"><b style="color:#333">Project name</b><br>Lorem Ipsum is simply dummy unknown printer took a galley of type and scrambled it to make.</p>
    <div class="abs display" style="left:354px;top:70px;width:72px;height:18px;background:var(--green);color:#fff;font-size:5px;text-align:center;line-height:18px">ADD YOUR TITLE</div>
    <p class="abs tiny" style="left:358px;top:94px;width:64px"><b style="color:#333">Project name</b><br>Lorem Ipsum is simply dummy unknown printer took a galley of type and scrambled it.</p>
    <p class="abs tiny" style="left:358px;top:140px;width:64px"><b style="color:#333">Project name</b><br>Lorem Ipsum is simply dummy unknown printer took a galley of type and scrambled it.</p>
    <div class="mark"><i></i><b>VELMORA ENERGY</b></div>
    <div class="page-tab">PAGE |18</div>
  </section>

  <!-- row 7 -->
  <section class="slide c1 r7">
    <p class="kicker" style="left:24px">HERE ADD YOUR TITLE</p><h3 class="slide-title" style="left:22px">ADD YOUR TITLE HERE</h3><span class="title-rule" style="left:24px"></span>
    <p class="abs display" style="left:34px;top:58px;font-size:5.5px;color:var(--navy)">LOREM IPSUM</p>
    <p class="abs display" style="left:150px;top:58px;font-size:5.5px;color:var(--navy)">LOREM IPSUM</p>
    <p class="abs display" style="left:266px;top:58px;font-size:5.5px;color:var(--navy)">LOREM IPSUM</p>
    <p class="abs tiny" style="left:34px;top:68px;width:100px;color:#444">• Lorem ipsum dolor sit amet, consectetur adipiscing elit.<br>• Lorem ipsum dolor sit amet, consectetur adipiscing elit. Maecas porttitor congue massa.</p>
    <p class="abs tiny" style="left:150px;top:68px;width:100px;color:#444">• Lorem ipsum dolor sit amet, consectetur adipiscing elit.<br>• Lorem ipsum dolor sit amet, consectetur adipiscing elit. Maecas porttitor congue massa.</p>
    <p class="abs tiny" style="left:266px;top:68px;width:100px;color:#444">• Lorem ipsum dolor sit amet, consectetur adipiscing elit.<br>• Lorem ipsum dolor sit amet, consectetur adipiscing elit. Maecas porttitor congue massa.</p>
    <table class="abs" style="left:18px;top:118px;width:420px;border-collapse:collapse;font-size:5px;color:#444;text-align:center">
      <tr style="border-top:1.5px solid var(--blue);border-bottom:1px solid var(--blue);height:14px;font-weight:600"><td>Text</td><td>Text</td><td>Text</td><td>Text</td><td>Text</td><td>Text</td></tr>
      <tr style="height:14.5px;background:#f0f1f2"><td>Data</td><td>Data</td><td>Data</td><td>Data</td><td>Data</td><td>Data</td></tr>
      <tr style="height:14.5px"><td>Data</td><td>Data</td><td>Data</td><td>Data</td><td>Data</td><td>Data</td></tr>
      <tr style="height:14.5px;background:#f0f1f2"><td>Data</td><td>Data</td><td>Data</td><td>Data</td><td>Data</td><td>Data</td></tr>
      <tr style="height:14.5px"><td>Data</td><td>Data</td><td>Data</td><td>Data</td><td>Data</td><td>Data</td></tr>
      <tr style="height:14.5px;background:#f0f1f2"><td>Data</td><td>Data</td><td>Data</td><td>Data</td><td>Data</td><td>Data</td></tr>
    </table>
    <div class="mark"><i></i><b>VELMORA ENERGY</b></div>
    <div class="page-tab">PAGE |19</div>
  </section>

  <section class="slide c2 r7" style="background:linear-gradient(180deg,#f7f8fa,#fff)">
    <div class="abs" style="left:0;top:0;width:456px;height:238px;background:linear-gradient(180deg,rgba(220,226,234,.5),rgba(255,255,255,.2))" role="img" aria-label="Faint team photo background"></div>
    <div class="logo abs" style="left:0;top:42px;width:456px"><i style="width:46px;height:46px"></i><b style="font-size:9px">VELMORA ENERGY</b></div>
    <h2 class="abs display" style="left:0;top:146px;width:456px;text-align:center;color:var(--blue);font-size:13px;font-weight:400">ADD YOUR AWESOME TITLE HERE</h2>
    <p class="abs" style="left:0;top:161px;width:456px;text-align:center;color:var(--green);font-size:6.5px;letter-spacing:3px">SUBTITLE GOES HERE</p>
    <p class="abs tiny" style="left:88px;top:185px;width:280px;text-align:center;color:#333">Lorem ipsum dolor sit amet, consectetur adipiscing elit, sed do eiusmod tempor incididunt ut labore et dolore magna aliqua. Lorem ipsum dolor sit amet, consectetur adipiscing elit, sed do eiusmod tempor incididunt ut labore et dolore magna aliqua.</p>
    <div class="abs" style="left:0;top:238px;width:456px;height:19px;background:var(--blue-deep)"></div>
    <p class="abs display" style="left:0;top:243px;width:456px;text-align:center;color:#fff;font-size:6px;letter-spacing:3px">YOUR QUOTE GOES HERE</p>
  </section>

</div>
</body>
</html>
```